Showroom Signage Design – Bright Hinges (High-Exposure Road Frontage)

Project Overview
We are looking for a creative designer to develop large-scale external signage for the Bright Hinges showroom.
The building is a double-storey showroom with full glass frontage positioned on a very busy main road.
The glazing spans both levels and we want to utilise the façade like a large billboard that captures attention from passing traffic.
The design must be bold, clean, professional, and highly readable at speed.
About Bright Hinges:
Bright Hinges specialises in cabinetry face-lifts / renovations.
including:
Our Core Service — Cabinetry Facelifts
- Kitchens
- Bathrooms
- Laundries
- Wardrobes
We Also Offer New Installations:
- Kitchens
- Bathrooms
- Laundries
- Wardrobes
We want the signage to clearly communicate that we are experts in facelifting / renovating spaces, while also providing complete new cabinetry solutions.
We will remove the reflective film on the windows for the lower level. There will be a kitchen showing in the middle of the lower level. So we don't want signage infront of the kitchen area. (Attached is a screenshot of the office with blue and pink squares. The blue is the location of the kitchen internally, and the pink can be signage design spaces.) Ideally the printing wont have a solid colour background for printing on the lower level.
Design Goals:
- Turns the entire glazed frontage into a visual billboard
- Works across two storeys
- Is highly visible from passing vehicles
- Uses strong hierarchy and minimal clutter
- Clearly communicates our services at a glance
- Encourages customers to visit the showroom
Think impact first, then detail.
Key Considerations
- Viewed primarily by drive-by traffic
- Must read clearly from distance and speed
- Should utilise window graphics, scale, and layout effectively
- Design should enhance — not block — natural light where possible
- Must feel architectural and professional, not retail clutter
Deliverables:
Print-ready vector files (AI/EPS/PDF)
Building mockups showing real-world application
We are looking for a design that makes Bright Hinges impossible to miss — transforming the showroom frontage into a powerful advertising statement.
Target Market(s)
Renovation clients on a budget, but also clients wanting an efficient turn around of high end projects.
Colors
Designer to choose only greyscale colors for use in the design.
Look and feel

```html
<!DOCTYPE html>
<html lang="en">
<head>
<meta charset="utf-8">
<title>Bright Hinges – Showroom Frontage Signage</title>
<link rel="stylesheet" href="https://fonts.googleapis.com/css2?family=Montserrat:wght@500;600;700&display=swap">
<style>
:root{
  --page:#ffffff;
  --facade:#c9cbcc;
  --concrete:#b5b7b8;
  --panel:#38393b;
  --panel-deep:#2c2d2f;
  --glass:#4a4d50;
  --band:#e6e6e6;
  --ink:#333436;
  --white:#f4f4f4;
  --rule:#8a8c8e;
}
*{box-sizing:border-box;margin:0;padding:0}
html,body{width:1200px;height:1200px;overflow:hidden;background:var(--page)}
body{position:relative;font-family:"Montserrat",sans-serif;color:var(--white)}
.abs{position:absolute;white-space:nowrap}

.facade{left:109px;top:180px;width:989px;height:464px;background:var(--facade)}
.ground{left:0;bottom:0;width:100%;height:70px;background:var(--concrete)}

.panel{background:var(--panel)}
.hero{left:52px;top:48px;width:391px;height:209px}
.hero-name{left:20px;top:26px;font-weight:700;font-size:36px;letter-spacing:.3px;line-height:1}
.hero-tag{left:22px;top:80px;font-weight:600;font-size:12.5px;letter-spacing:1.5px;line-height:1}
.hero-band{left:0;top:108px;width:100%;height:32px;background:var(--band);color:var(--ink);
  font-weight:600;font-size:11px;letter-spacing:2px;text-align:center;line-height:32px}

.services{display:flex;left:0;width:100%}
.service{flex:1;display:flex;flex-direction:column;align-items:center;gap:6px;border-left:1px solid var(--rule)}
.service:first-child{border-left:none}
.service-icon{width:34px;height:36px;background:#6d6f72;border-radius:3px}
.service-label{font-weight:600;font-size:8.5px;letter-spacing:.4px}
.hero .services{top:148px;height:56px}

.window-low{left:52px;top:260px;width:391px;height:116px;background:var(--glass)}
.kitchen-view{left:170px;top:0;width:221px;height:116px;background:linear-gradient(90deg,#55585b,#7a6f60 55%,#5c5a56)}
.slogan{left:26px;top:26px;font-weight:600;font-size:15px;line-height:22px}
.slogan-rule{left:26px;top:96px;width:94px;height:1px;background:var(--white)}

.feature{left:465px;top:117px;width:171px;height:115px;background:#5c5f62}
.feature-text{left:13px;top:24px;font-weight:600;font-size:11px;line-height:17.5px;letter-spacing:.3px}
.feature-rule{left:13px;top:98px;width:66px;height:1px;background:var(--white)}

.entry{left:465px;top:282px;width:171px;height:107px;background:var(--panel-deep)}
.door{top:6px;width:36px;height:101px;border:2px solid #8d9093;background:#3f4245}

.brand{left:673px;top:117px;width:316px;height:118px}
.brand-mark{left:18px;top:30px;width:46px;height:46px;border:3px solid var(--white)}
.brand-name{left:80px;top:26px;font-weight:700;font-size:21px;letter-spacing:.3px}
.brand-lines{left:80px;top:57px;font-weight:500;font-size:10.5px;line-height:16px;letter-spacing:.8px}
.brand-note{left:80px;top:95px;font-weight:500;font-size:7.5px;letter-spacing:.5px}

.solutions{left:673px;top:264px;width:316px;height:121px}
.solutions-title{left:14px;top:11px;font-weight:600;font-size:11px;letter-spacing:.3px}
.solutions-rule{left:0;top:33px;width:100%;height:1px;background:var(--rule)}
.solutions .services{top:40px;height:56px}
.visit{left:0;bottom:0;width:100%;height:22px;background:var(--band);color:var(--ink);
  font-weight:600;font-size:10px;letter-spacing:.8px;line-height:22px;padding-left:28px}

.identity{left:109px;top:666px;width:358px;height:345px;background:var(--page);color:var(--ink)}
.id-row{left:0;top:160px;width:100%;display:flex;justify-content:center;align-items:center;gap:10px}
.id-mark{width:24px;height:24px;border:3px solid var(--ink)}
.id-name{font-weight:700;font-size:25px;letter-spacing:.8px;line-height:1}
.id-rule{left:68px;top:200px;width:226px;height:1.5px;background:var(--ink)}
.id-tag{left:0;top:213px;width:100%;text-align:center;font-weight:500;font-size:12px;letter-spacing:2.2px;line-height:18px}
.promise{left:0;top:274px;width:100%;height:71px;background:var(--panel);display:flex;align-items:center}
.promise-item{flex:1;display:flex;flex-direction:column;align-items:center;gap:5px;border-left:1px solid var(--rule);color:var(--white)}
.promise-item:first-child{border-left:none}
.promise-label{font-weight:600;font-size:7px;letter-spacing:.4px;text-align:center;line-height:9px}

.street-view{left:475px;top:667px;width:623px;height:335px;background:linear-gradient(180deg,#c9d3dc 0%,#dfe3e6 35%,#6d7072 62%,#55585a 100%)}
</style>
</head>
<body>

<section class="abs facade" aria-label="Showroom frontage signage layout">
  <div class="abs ground"></div>

  <div class="abs panel hero">
    <div class="abs hero-name">BRIGHT HINGES</div>
    <div class="abs hero-tag">FACELIFT. TRANSFORM. LOVE YOUR SPACE.</div>
    <div class="abs hero-band">CABINETRY FACELIFTS</div>
    <div class="abs services">
      <div class="service"><div class="service-icon" role="img" aria-label="kitchen cabinet icon"></div><span class="service-label">KITCHENS</span></div>
      <div class="service"><div class="service-icon" role="img" aria-label="bathroom vanity icon"></div><span class="service-label">BATHROOMS</span></div>
      <div class="service"><div class="service-icon" role="img" aria-label="laundry cabinet icon"></div><span class="service-label">LAUNDRIES</span></div>
      <div class="service"><div class="service-icon" role="img" aria-label="wardrobe icon"></div><span class="service-label">WARDROBES</span></div>
    </div>
  </div>

  <div class="abs window-low">
    <div class="abs kitchen-view" role="img" aria-label="display kitchen seen through the lower glazing"></div>
    <div class="abs slogan">NEW LOOK.<br>SAME SPACE.<br>BETTER LIFE.</div>
    <div class="abs slogan-rule"></div>
  </div>

  <div class="abs feature">
    <div class="abs feature-text">EXPERTS IN<br>FACELIFTING<br>&amp; RENOVATING<br>SPACES</div>
    <div class="abs feature-rule"></div>
  </div>

  <div class="abs entry">
    <div class="abs door" style="left:8px"></div>
    <div class="abs door" style="left:46px"></div>
    <div class="abs door" style="left:89px"></div>
    <div class="abs door" style="left:127px"></div>
  </div>

  <div class="abs panel brand">
    <div class="abs brand-mark"></div>
    <div class="abs brand-name">BRIGHT HINGES</div>
    <div class="abs brand-lines">KITCHENS. BATHROOMS.<br>LAUNDRIES. WARDROBES.</div>
    <div class="abs brand-note">FACELIFTS &amp; NEW INSTALLATIONS</div>
  </div>

  <div class="abs panel solutions">
    <div class="abs solutions-title">COMPLETE SOLUTIONS. STUNNING RESULTS.</div>
    <div class="abs solutions-rule"></div>
    <div class="abs services">
      <div class="service"><div class="service-icon" role="img" aria-label="kitchen cabinet icon"></div><span class="service-label">KITCHENS</span></div>
      <div class="service"><div class="service-icon" role="img" aria-label="bathroom vanity icon"></div><span class="service-label">BATHROOMS</span></div>
      <div class="service"><div class="service-icon" role="img" aria-label="laundry cabinet icon"></div><span class="service-label">LAUNDRIES</span></div>
      <div class="service"><div class="service-icon" role="img" aria-label="wardrobe icon"></div><span class="service-label">WARDROBES</span></div>
    </div>
    <div class="abs visit">VISIT OUR SHOWROOM TODAY &nbsp;&#8594;</div>
  </div>
</section>

<section class="abs identity" aria-label="Brand identity">
  <div class="abs id-row"><span class="id-mark"></span><span class="id-name">BRIGHT HINGES</span></div>
  <div class="abs id-rule"></div>
  <div class="abs id-tag">FACELIFT. TRANSFORM.<br>LOVE YOUR SPACE.</div>
  <div class="abs promise">
    <div class="promise-item">
      <svg width="24" height="24" viewBox="0 0 24 24" fill="none" stroke="#f4f4f4" stroke-width="1.6" role="img" aria-label="speech bubble icon"><path d="M12 3a9 8 0 1 0-4.5 14.9L5 21l4.3-2.2A9 8 0 1 0 12 3z"/><circle cx="8" cy="11" r=".6" fill="#f4f4f4"/><circle cx="12" cy="11" r=".6" fill="#f4f4f4"/><circle cx="16" cy="11" r=".6" fill="#f4f4f4"/></svg>
      <span class="promise-label">EXPERT<br>ADVICE</span>
    </div>
    <div class="promise-item">
      <svg width="24" height="24" viewBox="0 0 24 24" fill="none" stroke="#f4f4f4" stroke-width="1.6" role="img" aria-label="tick icon"><circle cx="12" cy="12" r="9"/><path d="M8 12.5l3 3 5-6"/></svg>
      <span class="promise-label">QUALITY<br>FINISHES</span>
    </div>
    <div class="promise-item">
      <svg width="24" height="24" viewBox="0 0 24 24" fill="none" stroke="#f4f4f4" stroke-width="1.6" role="img" aria-label="timer icon"><circle cx="13" cy="13" r="8"/><path d="M13 9v4l3 2M11 3h4M2 11h4M3 15h3"/></svg>
      <span class="promise-label">FAST<br>TRANSFORMATION</span>
    </div>
    <div class="promise-item">
      <svg width="24" height="24" viewBox="0 0 24 24" fill="none" stroke="#f4f4f4" stroke-width="1.6" role="img" aria-label="shield with tick icon"><path d="M12 3l7 3v6c0 4.5-3 7.5-7 9-4-1.5-7-4.5-7-9V6z"/><path d="M8.5 12l2.5 2.5 4.5-5"/></svg>
      <span class="promise-label">MADE TO<br>LAST</span>
    </div>
  </div>
</section>

<div class="abs street-view" role="img" aria-label="street view of the showroom frontage with signage applied, by a main road intersection"></div>

</body>
</html>
```